Engineering group involved with fire safety needs a business card

We need a business card design for a company based in Greece called "Varotis Group". We are engineers and specialized technicians, operating the following : a) Fire fighting equipment trade b) Installation , Inspection & Maintenance of fire extinguishers and fire protection systems c) Occupational Health & Safety (Risk assessment & management/ Staff training). We need a clear and simple card design. I uploaded a draft I made, in order to give you an idea of the company and how I currently imagine the design of the card. I also uploaded the logo in .png file format. We are always open to different, new suggestions and ideas you may want to submit.
Target Market(s)
industries, companies, managers, retail clients
Industry/Entity Type
Fire Safety
Contact Information for Business Card
Addresses & phone numbers (headquarters + branch), logo, name (you can find all the details on the uploaded files!)
Colors
Designer to choose colors to be used in the design.
Look and feel
Each slider illustrates characteristics of the customer's brand and the style your logo design should communicate.

```html
<!DOCTYPE html>
<html lang="en">
<head>
<meta charset="utf-8">
<title>Varotis Group — Business Card</title>
<link href="https://fonts.googleapis.com/css2?family=Arimo:wght@400;700&display=swap" rel="stylesheet">
<style>
  :root {
    --stage-top: #2e2e2e;
    --stage-bottom: #0e0e0e;
    --card: #1d1d1d;
    --ink: #ffffff;
    --ink-soft: #e6e6e6;
    --emboss: #6e6e6e;
    --emboss-soft: #8a8a8a;
  }
  * { box-sizing: border-box; margin: 0; padding: 0; }
  html, body { width: 1200px; height: 900px; overflow: hidden; }
  body {
    background: radial-gradient(ellipse at 60% 10%, var(--stage-top), var(--stage-bottom) 75%);
    font-family: "Arimo", Arial, sans-serif;
    position: relative;
  }
  .card {
    position: absolute;
    left: 268px;
    width: 664px;
    height: 380px;
    background: var(--card);
    box-shadow: 0 12px 30px rgba(0,0,0,.55);
  }
  .card--front { top: 45px; }
  .card--back { top: 470px; }

  /* Front */
  .front-brand {
    position: absolute; left: 0; right: 0; top: 120px;
    display: flex; align-items: center; justify-content: center; gap: 16px;
  }
  .brand-mark { width: 34px; height: 34px; background: currentColor; }
  .front-brand { color: var(--emboss); }
  .brand-name {
    font-weight: 700; font-size: 52px; letter-spacing: 1px; text-transform: uppercase;
  }
  .front-tagline {
    position: absolute; left: 0; right: 0; top: 230px; text-align: center;
    color: var(--emboss-soft); font-size: 17px; letter-spacing: .3px;
  }
  .front-tagline .sep { font-size: 11px; margin: 0 8px; vertical-align: 2px; }

  /* Back */
  .back-brand {
    position: absolute; left: 36px; top: 130px; width: 270px; color: var(--ink);
  }
  .back-brand .brand-row { display: flex; align-items: center; gap: 12px; }
  .back-brand .brand-mark { width: 26px; height: 26px; }
  .back-brand .brand-name { font-size: 35px; letter-spacing: .5px; }
  .back-tagline { margin-top: 14px; font-size: 17px; color: var(--ink-soft); }
  .divider {
    position: absolute; left: 326px; top: 60px; width: 2px; height: 250px; background: var(--ink);
  }
  .contact { position: absolute; left: 350px; top: 62px; color: var(--ink); }
  .person { font-weight: 700; font-size: 22px; letter-spacing: .3px; }
  .role { font-size: 15px; line-height: 1.2; margin-top: 4px; color: var(--ink-soft); }
  .lines { list-style: none; margin-top: 20px; }
  .lines li { display: flex; align-items: center; gap: 10px; font-size: 14px; line-height: 19px; }
  .lines svg { width: 14px; height: 14px; flex: none; stroke: var(--ink); fill: none; stroke-width: 1.4; }
  .addresses { margin-top: 6px; font-size: 14px; line-height: 19px; }
</style>
</head>
<body>
  <section class="card card--front">
    <div class="front-brand">
      <span class="brand-mark"></span>
      <span class="brand-name">Varotis Group</span>
    </div>
    <p class="front-tagline">Installation<span class="sep">◆</span>Inspection<span class="sep">◆</span>Maintenance</p>
  </section>

  <section class="card card--back">
    <div class="back-brand">
      <div class="brand-row">
        <span class="brand-mark"></span>
        <span class="brand-name">Varotis Group</span>
      </div>
      <p class="back-tagline">installation-inspection-maintenance</p>
    </div>
    <div class="divider"></div>
    <div class="contact">
      <h1 class="person">Stavros Varotis</h1>
      <p class="role">Mechanical Engineer -<br>OHS Consultant</p>
      <ul class="lines">
        <li><svg viewBox="0 0 16 16"><path d="M3 2l3 1 1 3-2 1c1 2 2 3 4 4l1-2 3 1 1 3c-6 1-12-5-11-11z"/></svg>(HQ) +30 22990 41528</li>
        <li><svg viewBox="0 0 16 16"><path d="M3 2l3 1 1 3-2 1c1 2 2 3 4 4l1-2 3 1 1 3c-6 1-12-5-11-11z"/></svg>(BO) +30 210 6142937</li>
        <li><svg viewBox="0 0 16 16"><rect x="4" y="1" width="8" height="14" rx="1.5"/><path d="M7 12.5h2"/></svg>+30 694 215 73 80</li>
        <li><svg viewBox="0 0 16 16"><rect x="1" y="3" width="14" height="10"/><path d="M1 3l7 6 7-6"/></svg>info@varotisgroup.gr</li>
        <li><svg viewBox="0 0 16 16"><rect x="1" y="3" width="14" height="10"/><path d="M1 3l7 6 7-6"/></svg>stavros.varotis@varotisgroup.gr</li>
        <li><svg viewBox="0 0 16 16"><circle cx="8" cy="8" r="7"/><path d="M1 8h14M8 1c-3 4-3 10 0 14M8 1c3 4 3 10 0 14"/></svg>www.varotisgroup.gr</li>
      </ul>
      <p class="addresses">Headquarters: 12 Ilionos Street, 19400 Keratea<br>Branch Office: Anemonis Street, 15233 Chalandri</p>
    </div>
  </section>
</body>
</html>
```